Informative poster of frozen yogurt prices and sizes

Product is Frozen Yogurt. Need a menu poster A1/A0 size. Graphics showing 3 cup sizes (small $4, Medium $6 & Large $8). Extra 50Cent for each toppings (toppings includes stawberries, kiwi, nuts, candy etc.
for similar concept please refer to www.velmorasweets.com .
Design has to be clear and not too complicated

Target Market(s)

The poster is to be located at high traffic area. therefore it has to be very clear and precise and eye catching

Industry/Entity Type

Product

Requirements
Must have
• graphics of frozen yogurt cup, a variety of topping with prices. The prices has to be bold and clear. Easy to understand and not complicated.
Nice to have
• concept of value for money and healthy option dessert
Should not have
• too complicated background graphic

```html
<!DOCTYPE html>
<html lang="en">
<head>
<meta charset="utf-8">
<title>Frozen Yogurt Menu</title>
<link rel="stylesheet" href="https://fonts.googleapis.com/css2?family=Great+Vibes&family=Alfa+Slab+One&family=Signika:wght@700&family=Archivo+Black&family=Arimo:wght@700&display=swap">
<style>
  :root {
    --pink: #e0185f;
    --pink-soft: #f06aa4;
    --magenta: #c2107a;
    --purple: #7d2a8c;
    --sky: #cdeaf7;
    --sky-deep: #a9d8ef;
    --brown: #3b302b;
    --lime: #8ee21b;
    --yellow: #f3e521;
    --white: #ffffff;
    --cup: #b0175f;
  }
  * { margin: 0; padding: 0; box-sizing: border-box; }
  html, body { width: 812px; height: 1200px; overflow: hidden; background: #e6e6e6; }
  .poster { position: relative; width: 812px; height: 1200px; background: var(--white); overflow: hidden; }

  .header { position: absolute; left: 0; top: 0; width: 812px; height: 242px; background: var(--white); }
  .header-photo { position: absolute; left: 0; top: 0; width: 270px; height: 242px;
    background: radial-gradient(ellipse at 40% 55%, #fbf6ec 0%, #efe3d3 45%, #f6c86a 70%, #ffffff 100%); }
  .title-script { position: absolute; left: 270px; top: 40px; font-family: "Great Vibes", cursive;
    font-size: 104px; color: var(--pink); line-height: 1; }
  .title-main { position: absolute; left: 292px; top: 120px; font-family: "Alfa Slab One", serif;
    font-size: 104px; color: var(--pink); line-height: 1; letter-spacing: 1px; }
  .band { position: absolute; left: 0; top: 242px; width: 812px; height: 30px;
    background: linear-gradient(180deg, var(--pink-soft), #e8508f); }

  .offer { position: absolute; left: 0; top: 272px; width: 812px; height: 432px;
    background: radial-gradient(ellipse at 30% 40%, #f2fbff 0%, var(--sky) 55%, var(--sky-deep) 100%); }
  .tagline { position: absolute; left: 205px; top: 310px; font-family: "Signika", sans-serif; font-size: 52px; line-height: 1.02; }
  .tagline .yummy { color: var(--magenta); display: block; padding-left: 38px; }
  .tagline .healthy { color: var(--purple); display: block; }

  .size { position: absolute; }
  .size svg { display: block; }
  .price-badge { position: absolute; border-radius: 50%; background: var(--white); border: 2px solid var(--pink);
    color: var(--pink); font-family: "Archivo Black", sans-serif; display: flex; align-items: center; justify-content: center; }
  .price-badge sup { font-size: 0.45em; margin-top: -0.6em; }

  .cups-photo { position: absolute; left: 330px; top: 410px; width: 482px; height: 360px;
    background: linear-gradient(180deg, #e9d6c8 0%, #f4eee6 30%, #c82a83 58%, #a0145e 100%);
    border-radius: 40px 0 0 40px; }

  .topping-badge { position: absolute; left: 278px; top: 590px; width: 140px; height: 140px; border-radius: 50%;
    background: var(--white); text-align: center; color: var(--cup); }
  .topping-badge .amount { font-family: "Archivo Black", sans-serif; font-size: 70px; line-height: 1; display: block; margin-top: 14px; }
  .topping-badge .amount sup { font-size: 30px; vertical-align: top; }
  .topping-badge .label { font-family: "Arimo", sans-serif; font-size: 22px; display: block; }
  .plus { position: absolute; left: 226px; top: 600px; font-family: "Archivo Black", sans-serif; font-size: 110px; color: var(--pink); line-height: 1; }

  .toppings { position: absolute; left: 0; top: 704px; width: 812px; height: 496px; background: var(--brown); }
  .section-title { position: absolute; left: 70px; font-family: "Archivo Black", sans-serif; font-size: 36px; letter-spacing: 0.5px; }
  .section-title.fruit { top: 790px; color: var(--lime); }
  .section-title.dry { top: 962px; color: var(--yellow); }

  .row { position: absolute; left: 0; width: 812px; }
  .row.fruit { top: 840px; }
  .row.dry { top: 1012px; }
  .item { position: absolute; width: 110px; margin-left: -55px; text-align: center; }
  .item .thumb { width: 74px; height: 74px; border-radius: 50%; margin: 0 auto; border: 3px solid var(--white); }
  .item .name { font-family: "Arimo", sans-serif; font-size: 20px; color: var(--white); margin-top: 8px; }
  .thumb.kiwi { background: radial-gradient(circle, #c8d94a 0%, #8fa62b 60%, #6b7a2a 100%); }
  .thumb.berry { background: radial-gradient(circle, #f0414e 0%, #c8102e 65%, #8e0d22 100%); }
  .thumb.cone { background: radial-gradient(circle, #f5e3c2 0%, #d9b07a 60%, #b88650 100%); }
  .thumb.candy { background: radial-gradient(circle, #f6c22a 0%, #3f9bd8 45%, #e0402b 75%, #4b9a3a 100%); }
</style>
</head>
<body>
<main class="poster">
  <header class="header">
    <div class="header-photo" role="img" aria-label="Photo of a frozen yogurt cup with soft-serve swirl and mango and kiwi pieces"></div>
    <div class="title-script">Frozen</div>
    <h1 class="title-main">YOGURT</h1>
  </header>
  <div class="band"></div>

  <section class="offer">
  </section>

  <div class="size size-small" style="left:38px;top:362px;">
    <svg width="80" height="56" viewBox="0 0 80 56"><path d="M2 4 H78 L70 54 H10 Z" fill="var(--pink)"/><rect x="0" y="0" width="80" height="8" rx="3" fill="var(--pink)"/><text x="40" y="35" text-anchor="middle" font-family="Arimo, sans-serif" font-weight="700" font-size="12" fill="#fff">SMALL</text></svg>
  </div>
  <div class="price-badge" style="left:114px;top:354px;width:52px;height:52px;font-size:30px;"><sup>$</sup>4</div>

  <div class="size size-medium" style="left:30px;top:440px;">
    <svg width="104" height="72" viewBox="0 0 104 72"><path d="M2 5 H102 L92 70 H12 Z" fill="var(--pink)"/><rect x="0" y="0" width="104" height="10" rx="4" fill="var(--pink)"/><text x="52" y="44" text-anchor="middle" font-family="Arimo, sans-serif" font-weight="700" font-size="15" fill="#fff">MEDIUM</text></svg>
  </div>
  <div class="price-badge" style="left:136px;top:440px;width:58px;height:58px;font-size:34px;"><sup>$</sup>6</div>

  <div class="size size-large" style="left:28px;top:540px;">
    <svg width="134" height="100" viewBox="0 0 134 100"><path d="M2 6 H132 L118 98 H16 Z" fill="var(--pink)"/><rect x="0" y="0" width="134" height="13" rx="5" fill="var(--pink)"/><text x="67" y="50" text-anchor="middle" font-family="Arimo, sans-serif" font-weight="700" font-size="22" fill="#fff">LARGE</text></svg>
  </div>
  <div class="price-badge" style="left:160px;top:600px;width:62px;height:62px;font-size:36px;"><sup>$</sup>8</div>

  <div class="tagline"><span class="yummy">Yummy</span><span class="healthy">Healthy</span></div>

  <div class="cups-photo" role="img" aria-label="Photo of four frozen yogurt cups in magenta cups with chocolate, peach, fruit and sprinkle toppings"></div>

  <section class="toppings"></section>

  <div class="plus">+</div>
  <div class="topping-badge"><span class="amount"><sup>$</sup>2</span><span class="label">TOPPING</span></div>

  <h2 class="section-title fruit">FRESH FRUIT TOPPING</h2>
  <div class="row fruit">
    <div class="item" style="left:95px"><div class="thumb kiwi" role="img" aria-label="Kiwi pieces"></div><div class="name">Name</div></div>
    <div class="item" style="left:210px"><div class="thumb berry" role="img" aria-label="Raspberries"></div><div class="name">Name</div></div>
    <div class="item" style="left:325px"><div class="thumb kiwi" role="img" aria-label="Kiwi pieces"></div><div class="name">Name</div></div>
    <div class="item" style="left:440px"><div class="thumb berry" role="img" aria-label="Raspberries"></div><div class="name">Name</div></div>
    <div class="item" style="left:570px"><div class="thumb kiwi" role="img" aria-label="Kiwi pieces"></div><div class="name">Name</div></div>
    <div class="item" style="left:695px"><div class="thumb berry" role="img" aria-label="Raspberries"></div><div class="name">Name</div></div>
  </div>

  <h2 class="section-title dry">DRY TOPPINGS</h2>
  <div class="row dry">
    <div class="item" style="left:95px"><div class="thumb cone" role="img" aria-label="Waffle cone pieces"></div><div class="name">Name</div></div>
    <div class="item" style="left:210px"><div class="thumb candy" role="img" aria-label="Coloured candies"></div><div class="name">Name</div></div>
    <div class="item" style="left:325px"><div class="thumb cone" role="img" aria-label="Waffle cone pieces"></div><div class="name">Name</div></div>
    <div class="item" style="left:440px"><div class="thumb candy" role="img" aria-label="Coloured candies"></div><div class="name">Name</div></div>
    <div class="item" style="left:570px"><div class="thumb cone" role="img" aria-label="Waffle cone pieces"></div><div class="name">Name</div></div>
    <div class="item" style="left:695px"><div class="thumb candy" role="img" aria-label="Coloured candies"></div><div class="name">Name</div></div>
  </div>
</main>
</body>
</html>
```